Stock Broking Firm - Web Design Project

We are looking at doing a full re-design of our home page and content page and moving the majority of our content over to DNN.

Phase 1 : Website redesign www.kpwealthdesk.com.au

The current design is too washed out, boring and has no call to action buttons.

Solution:

KP Wealthdesk is looking for a brighter/ cleaner redesign with a few stand out call to action buttons.

• Banner with logo across the top horizontally - Bright blue logo on white background similar to www.dailyledgerpress.com.au - CALL 1300 482 917 - Follow on Twitter / Facebook
• Horizontal menu bar - professional looking. - Home - About Us- Our Services - Membership - Open an Account - Become a member - Contact
• Below banner top left - large rotating banner - maybe zuvelo gallery style www.tallowhurst.com.au
• Right of rotating banner - Membership login
• Below members login - Register for Daily Market Report/ research blog - Large bright button / Name / Email / Phone / pop up??
• Below Register for daily market report - Market Indicies - RSS feed of delayed data from QNW see www.tallowhurst.com
• Below Market indicies - KP WEALTHDESK - Market Tweets ( feed from our twitter page)

Below Rotating Banner -

content area

Below content area - 4 large block buttons see www.greywickcapital.com.au ( hover over change colour)

Button 1 - EDUCATION - content - click here for more

Button 2 - Market Information and Research

Button 3 - Full service Broker - content brief - click here for more

Button 4 - Trade Commodities and Options

below buttons - small horizontal menu bar slightly different colour incl - Careers/ Partners / Legal Privacy FSG Site Map

Regards,
Colm Ashdown

Target Market(s)

35 - 65

Industry/Entity Type

Education

Requirements
Must have
• Follow brief above - large banner, call to action buttons, F.B. Twitter, Member login etc. 4 big buttons
Nice to have
• clean looking site similar to www.dailyledgerpress.com.au / not too busy. Corporate looking.
Should not have
• not too busy

```html
<!DOCTYPE html>
<html lang="en">
<head>
<meta charset="utf-8">
<title>KP Wealthdesk – Home</title>
<link href="https://fonts.googleapis.com/css2?family=Arimo:wght@400;700&display=swap" rel="stylesheet">
<style>
:root{
  --navy:#0b4468;
  --navy-dark:#06304c;
  --navy-band:#0f3f5f;
  --cyan:#3ab6e8;
  --charcoal:#3c3c3c;
  --tile-grey:#565656;
  --text:#222;
  --muted:#666;
  --panel-border:#dcdcdc;
  --row-alt:#e4e4e4;
  --red:#b8330f;
}
*{margin:0;padding:0;box-sizing:border-box}
html,body{width:1145px;height:1200px;overflow:hidden}
body{font-family:"Arimo",Arial,sans-serif;color:var(--text);background:#f3f3f3;position:relative}
.abs{position:absolute}
.top-band{left:0;top:0;width:1145px;height:466px;background:linear-gradient(180deg,#0a3552 0%,#16587e 60%,#0e4566 100%);border-top:7px solid #333}
.top-band-edge{left:0;top:461px;width:1145px;height:8px;background:#555}
.column{left:125px;top:7px;width:896px;height:1140px;background:#fff;box-shadow:0 0 18px rgba(0,0,0,.18)}

.call-box{left:725px;top:7px;width:277px;height:56px;background:var(--charcoal);border-radius:0 0 4px 4px;display:flex;align-items:center;justify-content:center;gap:8px;color:var(--cyan);font-size:22px;letter-spacing:.3px}
.follow{left:817px;top:84px;display:flex;align-items:center;gap:5px;font-size:17px;color:#111}
.follow .social{width:22px;height:22px;border-radius:4px;background:#2f78b8}
.follow .social:nth-child(3){background:#4fb0e4}
.follow .social:nth-child(4){background:#1c6aa5}

.brand{left:143px;top:36px}
.brand-name{font-size:40px;color:#1c5a80;font-weight:400;letter-spacing:-.5px;line-height:44px}
.brand-tag{font-size:9.5px;color:#555;text-align:right;line-height:12px;margin-top:3px}

.main-nav{left:142px;top:134px;width:860px;height:41px;background:linear-gradient(180deg,#135a84,#083b5b);border-radius:6px;display:flex;align-items:center;padding-left:8px;overflow:hidden}
.main-nav a{color:#fff;text-decoration:none;font-size:12.5px;padding:0 13px;height:41px;line-height:41px;white-space:nowrap;flex-shrink:0;border-right:1px solid #2c6c94}
.main-nav a:nth-child(7){border-right:none}
.search{margin-left:auto;margin-right:14px;flex-shrink:0;width:160px;height:21px;background:#f0f3f5;border-radius:3px;position:relative}
.search svg{position:absolute;right:6px;top:3px}

.slider{left:142px;top:187px;width:579px;height:225px;background:linear-gradient(120deg,#d8d4d0,#f3f1ee 45%,#c9c2bb 70%,#e7e3de)}
.slide-arrow{width:38px;height:38px;border-radius:50%;background:#333;display:flex;align-items:center;justify-content:center}

.panel{background:#fff;border:1px solid var(--panel-border);box-shadow:0 0 4px rgba(0,0,0,.08)}
.panel-head{height:32px;background:var(--navy);color:#fff;font-weight:700;font-size:17px;display:flex;align-items:center;gap:8px;padding-left:12px;white-space:nowrap}
.field{background:#fff;border:1px solid #cfcfcf;border-radius:2px;font-size:9px;color:#777;display:flex;align-items:center;gap:5px;padding-left:8px}
.btn-dark{background:linear-gradient(180deg,#4a4a4a,#111);color:#fff;font-weight:700;border-radius:3px;display:flex;align-items:center;justify-content:center}

.welcome-title{left:142px;top:436px;font-size:25px;font-weight:700;color:#4a4a4a;letter-spacing:-.5px}
.welcome-title span{color:var(--navy)}
.welcome-rule{left:142px;top:469px;width:551px;height:1px;background:#ccc}
.welcome-copy{left:142px;top:479px;width:569px;font-size:9.6px;line-height:11.9px;color:#222}
.welcome-copy p{margin-bottom:11px}

.tile{width:287px;height:130px;padding:11px 20px;color:#fff}
.tile.blue{background:var(--navy)}
.tile.grey{background:var(--tile-grey);color:#e6e6e6}
.tile h3{font-size:15px;font-weight:700;line-height:17px}
.tile h4{font-size:12px;font-weight:700;line-height:15px;letter-spacing:.3px}
.tile p{font-size:10.5px;line-height:13px;margin-top:8px;letter-spacing:.2px;width:250px}
.tile .more{font-size:9.5px;text-align:right;margin-top:2px;display:flex;justify-content:flex-end;align-items:center;gap:5px}
.tile .more i{width:9px;height:9px;border-radius:50%;background:#5fae3a;display:inline-block}

.indices table{width:255px;margin:8px 0 0 6px;border-collapse:collapse;font-size:11px}
.indices th{font-weight:400;text-align:left;height:26px;padding-left:8px}
.indices td{height:24.5px;padding-left:8px}
.indices tr:nth-child(even) td{background:var(--row-alt)}

.news{left:142px;top:926px;width:578px;height:191px}
.news-inner{position:absolute;left:10px;top:8px;width:559px;height:173px;background:#f1f1f1}
.news-title{position:absolute;left:45px;top:14px;font-size:22px;color:var(--navy)}
.news-rule{position:absolute;left:20px;top:44px;width:420px;border-top:1px dotted #999}
.news-photo{position:absolute;left:439px;top:9px;width:112px;height:69px;background:linear-gradient(135deg,#2c4e86,#8a2a2a 55%,#3f5e94);border:2px solid #2d6a96}
.news-head{position:absolute;left:20px;top:56px;font-size:11.5px}
.news-date{position:absolute;left:20px;top:77px;font-size:11px;color:var(--red)}
.news-body{position:absolute;left:20px;top:96px;width:535px;font-size:9.4px;line-height:11.6px;letter-spacing:-.2px}
.news-more{position:absolute;left:479px;top:144px;width:72px;height:21px;font-size:10px}

.tweets{left:736px;top:926px;width:267px;height:191px}
.tweets .panel-head{margin:4px 0 0 -4px;width:265px;height:34px}
.tweet{font-size:9.5px;line-height:12px;margin:0 8px 0 12px}
.tweet b{font-weight:400;color:#1a8ed0}

.footer{left:0;top:1147px;width:1145px;height:53px;background:var(--navy-band);border-top:4px solid #1a1a1a;color:#fff;font-size:10.5px}
.footer-links{position:absolute;left:140px;top:20px;display:flex;gap:6px}
.footer-copy{position:absolute;left:635px;top:20px}
</style>
</head>
<body>
<div class="abs top-band"></div>
<div class="abs top-band-edge"></div>
<div class="abs column"></div>

<header>
  <div class="abs brand">
    <div class="brand-name">KP Wealthdesk</div>
    <div class="brand-tag">shares | options | commodities | foreign exchange<br>ABN 47 302 118 650 | licence no 522 917</div>
  </div>
  <div class="abs call-box">
    <svg width="24" height="26" viewBox="0 0 24 26"><path d="M5 2c2 0 3 4 3 5s-2 2-2 3c1 3 4 7 7 8 1 0 2-2 3-2s5 1 5 3-3 4-5 4C10 22 2 12 2 6c0-2 1-4 3-4z" fill="none" stroke="#7fd0f0" stroke-width="2"/></svg>
    CALL 1300 482 917
  </div>
  <div class="abs follow">FOLLOW US :<span class="social"></span><span class="social"></span><span class="social"></span></div>
  <nav class="abs main-nav">
    <a href="#">Home</a><a href="#">About Us</a><a href="#">Our Services</a><a href="#">Membership</a><a href="#">Open an Account</a><a href="#">Become a member</a><a href="#">Contact</a>
    <div class="search"><svg width="15" height="15" viewBox="0 0 15 15"><circle cx="6" cy="6" r="4.5" fill="none" stroke="#999" stroke-width="1.5"/><path d="M9.5 9.5l4 4" stroke="#999" stroke-width="2"/></svg></div>
  </nav>
</header>

<div class="abs slider" role="img" aria-label="Banner photo of smiling office staff at a meeting table"></div>
<div class="abs slide-arrow" style="left:136px;top:274px"><svg width="16" height="14"><path d="M1 7h14M7 1L1 7l6 6" stroke="#fff" stroke-width="3" fill="none"/></svg></div>
<div class="abs slide-arrow" style="left:688px;top:274px"><svg width="16" height="14"><path d="M0 7h14M8 1l6 6-6 6" stroke="#fff" stroke-width="3" fill="none"/></svg></div>

<section class="abs panel" style="left:734px;top:187px;width:268px;height:224px">
  <div class="panel-head" style="margin:12px 0 0 -4px;width:265px"><svg width="22" height="18"><circle cx="7" cy="5" r="4" fill="#f2c27a"/><path d="M0 18c0-6 3-8 7-8s7 2 7 8z" fill="#fff"/><circle cx="16" cy="6" r="3.5" fill="#f2c27a"/><path d="M12 18c0-5 2-7 5-7s5 2 5 7z" fill="#cde"/></svg>MEMBERSHIP LOGIN</div>
  <div class="field abs" style="left:30px;top:56px;width:218px;height:30px">Username</div>
  <div class="field abs" style="left:30px;top:102px;width:218px;height:31px">Password</div>
  <div class="abs" style="left:30px;top:152px;font-size:9px;display:flex;align-items:center;gap:6px">
    <svg width="14" height="14"><rect x=".5" y=".5" width="13" height="13" fill="#fff" stroke="#bbb"/><path d="M3 7l3 3 5-7" stroke="#333" stroke-width="1.6" fill="none"/></svg>
    Remember me <span style="color:#bbb">⁝</span> <span style="color:#1a8ed0;text-decoration:underline">Forgot password</span>
  </div>
  <div class="abs btn-dark" style="left:54px;top:174px;width:194px;height:36px;font-size:20px">Login</div>
</section>

<h1 class="abs welcome-title">Welcome To <span>KP Wealthdesk</span></h1>
<div class="abs welcome-rule"></div>
<div class="abs welcome-copy">
  <p>Sed ut perspiciatis unde omnis iste natus error sit voluptatem accusantium doloremque laudantium, totam rem aperiam, eaque ipsa quae ab illo inventore veritatis et quasi architecto beatae vitae dicta sunt explicabo. Nemo enim ipsam voluptatem quia voluptas sit aspernatur aut odit aut fugit, sed quia consequuntur magni dolores eos qui ratione voluptatem sequi nesciunt. Neque porro quisquam est, qui dolorem ipsum quia dolor sit amet, consectetur, adipisci velit, sed quia non numquam eius modi tempora incidunt ut labore et dolore magnam aliquam quaerat voluptatem. Ut enim ad minima veniam, quis nostrum exercitationem ullam corporis suscipit laboriosam, nisi ut aliquid ex ea commodi consequatur? Quis autem vel eum iure reprehenderit qui in ea voluptate velit esse quam nihil molestiae consequatur, vel illum qui dolorem eum fugiat quo voluptas nulla pariatur?</p>
  <p>Sed ut perspiciatis unde omnis iste natus error sit voluptatem accusantium doloremque laudantium, totam rem aperiam, eaque ipsa quae ab illo inventore veritatis et quasi architecto beatae vitae dicta sunt explicabo. Nemo enim ipsam voluptatem quia voluptas sit aspernatur aut odit aut fugit, sed quia consequuntur magni dolores eos qui ratione voluptatem sequi nesciunt. Neque porro quisquam est, qui dolorem ipsum quia dolor sit amet, consectetur, adipisci velit, sed quia non numquam eius modi tempora</p>
</div>

<section class="abs panel" style="left:734px;top:430px;width:268px;height:202px">
  <div class="panel-head" style="margin:5px 0 0 -4px;width:265px;height:33px"><svg width="16" height="20"><rect x="1" y="1" width="14" height="18" fill="#fff" stroke="#9bb"/><rect x="4" y="11" width="2" height="6" fill="#3a8fd0"/><rect x="7" y="8" width="2" height="9" fill="#3a8fd0"/><rect x="10" y="5" width="2" height="12" fill="#3a8fd0"/></svg>DAILY MARKET REPORT</div>
  <div class="abs" style="left:0;top:52px;width:58px;text-align:right;font-size:9px;color:#555">User Name :</div>
  <div class="field abs" style="left:63px;top:47px;width:194px;height:21px"></div>
  <div class="abs" style="left:0;top:85px;width:58px;text-align:right;font-size:9.5px;color:#555">Email :</div>
  <div class="field abs" style="left:63px;top:80px;width:194px;height:21px"></div>
  <div class="abs" style="left:0;top:117px;width:58px;text-align:right;font-size:9.5px;color:#555">Phone :</div>
  <div class="field abs" style="left:63px;top:112px;width:194px;height:21px"></div>
  <div class="abs btn-dark" style="left:63px;top:149px;width:194px;height:36px;font-size:20px">Register</div>
</section>

<section class="abs tile blue" style="left:142px;top:646px">
  <h3>Education</h3><h4>Get Educational Info From Here</h4>
  <p>Lorem ipsum ex vix illud nonummy, novum tation et his. At vix scripta patrioque scribentur, at pro fugit verterem molestiae, sed et vivendo ali Lorem ipsum</p>
  <div class="more"><i></i>Learn More</div>
</section>
<section class="abs tile grey" style="left:433px;top:646px;padding-top:15px">
  <h3>Market Information and Research</h3><h4>Get Market Info From Here</h4>
  <p>Lorem ipsum ex vix illud nonummy, novum tation et his. At vix scripta patrioque scribentur, at pro fugit verterem molestiae, sed et vivendo ali Lorem ipsum</p>
  <div class="more"><i></i>Learn More</div>
</section>
<section class="abs tile grey" style="left:142px;top:780px">
  <h3>Full service Broker</h3><h4 style="font-weight:400;margin-top:7px">Get Info From Here</h4>
  <p>Lorem ipsum ex vix illud nonummy, novum tation et his. At vix scripta patrioque scribentur, at pro fugit verterem molestiae, sed et vivendo ali Lorem ipsum</p>
  <div class="more"><i></i>Learn More</div>
</section>
<section class="abs tile grey" style="left:433px;top:780px;padding-top:15px">
  <h3>Trade Commodities and Options</h3><h4>Get Market Info From Here</h4>
  <p>Lorem ipsum ex vix illud nonummy, novum tation et his. At vix scripta patrioque scribentur, at pro fugit verterem molestiae, sed et vivendo ali Lorem ipsum</p>
  <div class="more"><i></i>Learn More</div>
</section>

<section class="abs panel indices" style="left:734px;top:646px;width:268px;height:264px;background:#f0f0f0">
  <div class="panel-head" style="height:38px;gap:10px"><svg width="30" height="26"><rect x="0" y="12" width="8" height="14" fill="#e8751a"/><rect x="10" y="6" width="8" height="20" fill="#f2b517"/><rect x="20" y="0" width="8" height="26" fill="#5caf2e"/></svg>MARKET INDICIES</div>
  <table>
    <tr><th>Name</th><th>Value</th><th>+/-</th><th>%+/-</th></tr>
    <tr><td>All Ords</td><td>4,502.00</td><td>-11.80</td><td>-0.26</td></tr>
    <tr><td>All Ords</td><td>4,502.00</td><td>-11.80</td><td>-0.26</td></tr>
    <tr><td>All Ords</td><td>4,502.00</td><td>-11.80</td><td>-0.26</td></tr>
    <tr><td>All Ords</td><td>4,502.00</td><td>-11.80</td><td>-0.26</td></tr>
    <tr><td>All Ords</td><td>4,502.00</td><td>-11.80</td><td>-0.26</td></tr>
    <tr><td>All Ords</td><td>4,502.00</td><td>-11.80</td><td>-0.26</td></tr>
    <tr><td>All Ords</td><td>4,502.00</td><td>-11.80</td><td>-0.26</td></tr>
  </table>
</section>

<section class="abs panel news">
  <div class="news-inner">
    <svg style="position:absolute;left:12px;top:15px" width="28" height="20"><rect x="1" y="1" width="26" height="18" fill="#eee" stroke="#888"/><rect x="4" y="4" width="8" height="6" fill="#999"/><path d="M14 5h10M14 8h10M4 13h20M4 16h20" stroke="#888"/></svg>
    <div class="news-title">Latest News</div>
    <div class="news-rule"></div>
    <div class="news-photo" role="img" aria-label="Photo of a busy trading floor"></div>
    <div class="news-head">Sed ut perspiciatis unde omnis iste natus error sit voluptatem</div>
    <div class="news-date">Thursday, 16 August 2012</div>
    <div class="news-body">Sed ut perspiciatis unde omnis iste natus error sit voluptatem accusantium doloremque laudantium, totam rem aperiam, eaque ipsa quae ab illo inventore veritatis et quasi architecto beatae vitae dicta sunt explicabo. Nemo enim ipsam voluptatem quia voluptas sit aspernatur aut odit aut fugit, sed quia consequuntur magni dolores eos qui ratione voluptatem sequi nesciunt. Neque porro quisquam est, qui dolorem ipsum quia dolor sit amet, consectetur, adipisci velit, sed quia non numquam eius modi</div>
    <div class="news-more btn-dark">Read More</div>
  </div>
</section>

<section class="abs panel tweets">
  <div class="panel-head" style="font-weight:400;font-size:17px"><svg width="22" height="24"><circle cx="11" cy="12" r="10" fill="#3a8fd0"/></svg>OUR <span style="color:var(--cyan)">TWEETS</span></div>
  <div style="background:#f1f1f1;margin:6px 6px 0 6px;height:140px;padding-top:8px">
    <p class="tweet"><b>@ Merrow</b> - Ready for the game with the peace symbol in ours hands and in my head.</p>
    <p class="tweet" style="margin-top:32px"><b>@ Merrow</b> - Ready for the game with the peace symbol in ours hands and in my head.</p>
    <p class="tweet" style="margin-top:24px"><b>@ Merrow</b> - Ready for the game with the peace symbol in ours hands and in my head.</p>
  </div>
</section>

<footer class="abs footer">
  <div class="footer-links"><span>CAREERS</span>•<span>PARTNERS</span>•<span>LEGAL</span>•<span>PRIVACY</span>•<span>FSG</span>•<span>DISCLAIMER</span>•<span>SITE MAP</span></div>
  <div class="footer-copy">© 2012 KP WEALTHDESK (QLD) PTY LTD, ALL RIGHTS RESERVED</div>
</footer>
</body>
</html>
```